A4 Folder presentation Design Project

A4 Folder presentation Design.

A4 presentation folder, need to have company logo on it and aligned with company colors

Uploaded my business cards as a reference

Target Market(s)

Business owners

Industry/Entity Type

Electrical

Font styles to use
Sans Serif

Requirements
Must have
• Company logo

Company colors
Orange R:240 G:86 B:47
Blue R:4 G:116 B:187
Dark Grey

```html
<!DOCTYPE html>
<html lang="en">
<head>
<meta charset="utf-8">
<title>Voltara – A4 Presentation Folder, Inside Spread</title>
<link rel="stylesheet" href="https://fonts.googleapis.com/css2?family=Arimo:wght@400;700&display=swap">
<style>
  :root {
    --stage: #e4e4e4;
    --panel-dark: #3a3938;
    --panel-mid: #4a4847;
    --panel-light: #565453;
    --pocket-orange: #f0562f;
    --pocket-orange-light: #f27a5c;
    --brand-blue: #0474bb;
    --text-light: #ecebea;
    --text-soft: #d6d4d2;
    --deco-tone: #42403e;
  }
  * { margin: 0; padding: 0; box-sizing: border-box; }
  html, body {
    width: 1200px;
    height: 800px;
    overflow: hidden;
    background: var(--stage);
    font-family: "Arimo", Arial, sans-serif;
  }
  .folder-spread {
    position: absolute;
    left: 63px;
    top: 20px;
    width: 1074px;
    height: 760px;
    display: flex;
  }
  .panel {
    position: relative;
    width: 537px;
    height: 760px;
    overflow: hidden;
  }
  .panel-left {
    background: linear-gradient(120deg, var(--panel-dark) 0%, var(--panel-dark) 45%, var(--panel-light) 100%);
    border-right: 1px solid #2a2928;
  }
  .panel-right {
    background: linear-gradient(120deg, #2e2d2c 0%, var(--panel-mid) 55%, var(--panel-light) 100%);
    border-top-right-radius: 22px;
  }
  .brand-block {
    position: absolute;
    top: 150px;
    left: 0;
    width: 100%;
    text-align: center;
  }
  .brand-name {
    display: inline-flex;
    align-items: center;
    gap: 10px;
    font-size: 40px;
    font-weight: 700;
    color: var(--brand-blue);
    letter-spacing: 1px;
  }
  .brand-dot {
    width: 18px;
    height: 18px;
    border-radius: 50%;
    background: var(--brand-blue);
  }
  .folder-title {
    margin-top: 28px;
    font-size: 15px;
    font-weight: 400;
    line-height: 1.35;
    color: var(--text-light);
    text-transform: uppercase;
    letter-spacing: 0.5px;
  }
  .usp-list {
    list-style: none;
    margin-top: 34px;
    color: var(--text-soft);
    font-size: 12px;
    line-height: 1.4;
  }
  .usp-divider {
    width: 8px;
    height: 8px;
    margin: 12px auto;
    border-radius: 50%;
    background: var(--pocket-orange);
  }
  .deco-circle {
    position: absolute;
    right: -120px;
    top: 150px;
    width: 300px;
    height: 300px;
    border-radius: 50%;
    background: var(--deco-tone);
    opacity: 0.8;
  }
  .pocket {
    position: absolute;
    left: 0;
    bottom: 0;
    width: 100%;
    height: 300px;
    background: linear-gradient(115deg, #c9492a 0%, var(--pocket-orange) 35%, var(--pocket-orange-light) 65%, var(--pocket-orange) 100%);
    box-shadow: 0 -4px 10px rgba(0,0,0,0.25);
  }
</style>
</head>
<body>
  <main class="folder-spread">
    <section class="panel panel-left">
      <div class="brand-block">
        <div class="brand-name"><span class="brand-dot"></span>Voltara</div>
        <h1 class="folder-title">Here comes the title<br>USP's in the picture: for example</h1>
        <ul class="usp-list">
          <li>accredited master electrician<br>with monitored safety systems</li>
          <li class="usp-divider" aria-hidden="true"></li>
          <li>quality workmanship<br>at a fair and competitive price</li>
          <li class="usp-divider" aria-hidden="true"></li>
          <li>24/7 emergency response service<br>for your home or business</li>
        </ul>
      </div>
    </section>
    <section class="panel panel-right">
      <div class="deco-circle" aria-hidden="true"></div>
      <div class="pocket"></div>
    </section>
  </main>
</body>
</html>
```